cookie box packaging sleeve design

Hi,
I'm looking to create 5 sleeves for cookies in a box.
Classic look, not too many colors. I need to be able to add the nutrition info for each sleeve at the back.
width 110 mm height 370mm

1. Salted Tahini Choc-Chip Cookie
2. Brownie White Choc Cookie
3. Peanut Butter Cookie
4. Earthquake Cookie
5.Pistachio Cookie

ideas:
Biscotti by Tellanos (https://ryde.tellanos-example.com.au/?welcomed)
OR
https://au.snapboardia.com/pin/4820937715620384/

Target Market(s)

Family, office and for gifts

Industry/Entity Type

Cafe/Bakery

Colors

Designer to choose colors to be used in the design.

Requirements
Should not have
• Too many colours and the photo of the cookies

```html
<!DOCTYPE html>
<html lang="en">
<head>
<meta charset="utf-8">
<title>Bakerley House – Salted Tahini Choc-Chip Cookie Sleeve</title>
<link rel="stylesheet" href="https://fonts.googleapis.com/css2?family=Alfa+Slab+One&family=Rokkitt:wght@600&family=Yesteryear&display=swap">
<style>
  :root {
    --page: #ffffff;
    --pattern-tone: #e9edf0;
    --pattern-edge: #dfe6ea;
    --label-blue: #a4c2d6;
    --label-blue-deep: #9bbacf;
    --ink-light: #ffffff;
    --ribbon-ink: #a4c2d6;
  }
  * { margin: 0; padding: 0; box-sizing: border-box; }
  html, body {
    width: 1200px; height: 675px; overflow: hidden;
    background: var(--page);
  }
  .canvas {
    position: relative; width: 1200px; height: 675px;
  }
  .sleeve {
    position: absolute; left: 392px; top: 28px;
    width: 416px; height: 620px;
  }
  .sleeve-pattern {
    position: absolute; inset: 0;
    background: linear-gradient(180deg, var(--pattern-tone), var(--pattern-edge));
  }
  .label-panel {
    position: absolute; left: 22px; right: 22px; top: 258px; bottom: 0;
    background: linear-gradient(180deg, var(--label-blue-deep), var(--label-blue));
  }
  .scallop {
    position: absolute; left: 0; top: -7px; width: 100%; height: 8px; display: block;
  }
  .label-block {
    position: absolute; left: 0; right: 0;
    text-align: center; color: var(--ink-light);
  }
  .label-block--top { top: 22px; }
  .label-block--front { top: 192px; }
  .brand {
    display: inline-flex; align-items: center; gap: 8px;
    font-family: "Alfa Slab One", serif; font-size: 21px;
    letter-spacing: 0.5px; color: var(--ink-light);
  }
  .brand-dot {
    width: 8px; height: 8px; border-radius: 50%; background: var(--ink-light);
  }
  .product-name {
    margin-top: 12px;
    font-family: "Alfa Slab One", serif; font-size: 26px;
    line-height: 0.95; letter-spacing: 1.5px; text-transform: uppercase;
  }
  .claim-ribbon {
    display: inline-block; margin-top: 6px; padding: 1px 16px;
    background: var(--ink-light); border-radius: 2px;
    font-family: "Rokkitt", serif; font-size: 8px; font-weight: 600;
    letter-spacing: 1.6px; text-transform: uppercase; color: var(--ribbon-ink);
  }
  .tagline {
    margin-top: 6px;
    font-family: "Yesteryear", cursive; font-size: 17px;
  }
  .net-weight {
    margin-top: 6px;
    font-family: "Rokkitt", serif; font-size: 8px; font-weight: 600;
    letter-spacing: 1.6px;
  }
</style>
</head>
<body>
<main class="canvas">
  <section class="sleeve">
    <div class="sleeve-pattern" role="img" aria-label="Fine light blue lattice pattern on pale grey background"></div>

    <div class="label-panel">
      <svg class="scallop" viewBox="0 0 372 8" preserveAspectRatio="none" aria-hidden="true">
        <path fill="#9bbacf" d="M0 8 Q3.1 0 6.2 8 Q9.3 0 12.4 8 Q15.5 0 18.6 8 Q21.7 0 24.8 8 Q27.9 0 31 8 Q34.1 0 37.2 8 Q40.3 0 43.4 8 Q46.5 0 49.6 8 Q52.7 0 55.8 8 Q58.9 0 62 8 Q65.1 0 68.2 8 Q71.3 0 74.4 8 Q77.5 0 80.6 8 Q83.7 0 86.8 8 Q89.9 0 93 8 Q96.1 0 99.2 8 Q102.3 0 105.4 8 Q108.5 0 111.6 8 Q114.7 0 117.8 8 Q120.9 0 124 8 Q127.1 0 130.2 8 Q133.3 0 136.4 8 Q139.5 0 142.6 8 Q145.7 0 148.8 8 Q151.9 0 155 8 Q158.1 0 161.2 8 Q164.3 0 167.4 8 Q170.5 0 173.6 8 Q176.7 0 179.8 8 Q182.9 0 186 8 Q189.1 0 192.2 8 Q195.3 0 198.4 8 Q201.5 0 204.6 8 Q207.7 0 210.8 8 Q213.9 0 217 8 Q220.1 0 223.2 8 Q226.3 0 229.4 8 Q232.5 0 235.6 8 Q238.7 0 241.8 8 Q244.9 0 248 8 Q251.1 0 254.2 8 Q257.3 0 260.4 8 Q263.5 0 266.6 8 Q269.7 0 272.8 8 Q275.9 0 279 8 Q282.1 0 285.2 8 Q288.3 0 291.4 8 Q294.5 0 297.6 8 Q300.7 0 303.8 8 Q306.9 0 310 8 Q313.1 0 316.2 8 Q319.3 0 322.4 8 Q325.5 0 328.6 8 Q331.7 0 334.8 8 Q337.9 0 341 8 Q344.1 0 347.2 8 Q350.3 0 353.4 8 Q356.5 0 359.6 8 Q362.7 0 365.8 8 Q368.9 0 372 8 Z"/>
      </svg>

      <div class="label-block label-block--top">
        <div class="brand"><span class="brand-dot"></span>Bakerley House</div>
        <h2 class="product-name">Salted Tahini<br>Choc-Chip Cookie</h2>
        <div class="claim-ribbon">Gluten free &amp; dairy biscuits</div>
        <p class="tagline">Tradutional Italian Flourless almonds biscuits</p>
      </div>

      <div class="label-block label-block--front">
        <div class="brand"><span class="brand-dot"></span>Bakerley House</div>
        <h1 class="product-name">Salted Tahini<br>Choc-Chip Cookie</h1>
        <div class="claim-ribbon">Gluten free &amp; dairy biscuits</div>
        <p class="net-weight">300G</p>
      </div>
    </div>
  </section>
</main>
</body>
</html>
```